PICTURE CALENDAR - CONSTRUCTION COMPANY

- PICTURES CALENDAR 2018 (wall calendar) - graphic design - square 50 x 50 cm - 14 pages (title - months index pages) - languages ​​- german - Italian - construction industry - minimalistic and clear - modern - for each month inkluding logo color www.tovelbrunn.it
Updates

Project Deadline Extended
Reason: Sehr geehrte Damen und Herren, bitte um eine Fristverlängerung. Es ist Wochenende und ich selbst bekomme auf kein Feedback ob ein Design jetzt passt oder nicht. Weiters haben wir bereits einen Favoriten welcher aber noch Details abändern müsste. Vielen Dank! Mit freundlichen Grüßen, Matthias Kerber

Target Market(s)

construction worker

Industry/Entity Type

Construction

Font styles to use
Sans Serif

Colors
0355a3
dddddd

Requirements
Must have
• 49 x 49 cm 12 months german italiano short image description including logo
Nice to have
• cool line
Should not have
• the graphic design not playful, no gradients

```html
<!DOCTYPE html>
<html lang="de">
<head>
<meta charset="utf-8">
<title>Kalender 2018 – November</title>
<link rel="stylesheet" href="https://fonts.googleapis.com/css2?family=Arimo:ital,wght@0,400;0,700;1,400&family=Open+Sans:wght@600;700&display=swap">
<style>
  :root {
    --brand-blue: #0355a3;
    --mid-blue: #2f76bd;
    --light-grey: #eeeeee;
    --rule-grey: #b5b5b5;
    --ink: #111111;
    --white: #ffffff;
    --logo-navy: #2b3990;
  }
  * { margin: 0; padding: 0; box-sizing: border-box; }
  html, body { width: 1200px; height: 1200px; overflow: hidden; background: var(--white); }
  .page { position: relative; width: 1200px; height: 1200px; overflow: hidden; font-family: "Arimo", Arial, sans-serif; }

  .hero-photo {
    position: absolute; left: 0; top: 0; width: 1200px; height: 672px;
    background: linear-gradient(160deg, #c9c6c0 0%, #e6e6e4 30%, #58703f 55%, #7a6a55 80%, #6b5a48 100%);
  }
  .frame-shapes { position: absolute; left: 0; top: 0; width: 1200px; height: 1200px; }

  .description { position: absolute; left: 19px; top: 743px; width: 410px; color: var(--brand-blue); }
  .description-de { font-size: 16px; line-height: 20.7px; }
  .description-rule { width: 314px; height: 1px; background: var(--brand-blue); margin: 17px 0 10px 83px; }
  .description-en { font-size: 13.3px; line-height: 17.3px; font-style: italic; }

  .brand { position: absolute; left: 21px; top: 1059px; display: flex; align-items: center; gap: 14px; }
  .brand-square { width: 66px; height: 66px; background: var(--logo-navy); }
  .brand-name { font-size: 32px; font-weight: 700; color: var(--logo-navy); letter-spacing: -0.5px; }

  .web-address { position: absolute; left: 19px; top: 1144px; font-family: "Open Sans", sans-serif; font-weight: 700; font-size: 26px; color: var(--white); }

  .year { position: absolute; left: 551px; top: 735px; font-size: 97px; font-weight: 700; color: var(--mid-blue); letter-spacing: 1px; line-height: 1; }
  .month { position: absolute; right: 141px; top: 733px; text-align: right; line-height: 1; }
  .month-de { font-size: 48px; font-weight: 700; color: var(--brand-blue); }
  .month-it { font-size: 36px; font-style: italic; color: var(--mid-blue); margin-top: 4px; }

  .calendar { position: absolute; left: 551px; top: 849px; width: 508px; font-family: "Open Sans", sans-serif; }
  .weekend-bg { position: absolute; top: 18px; width: 72px; height: 299px; background: var(--light-grey); }
  .weekend-bg.sun { left: 0; }
  .weekend-bg.sat { left: 436px; }
  .calendar-grid { position: relative; display: grid; grid-template-columns: repeat(7, 72.6px); }
  .weekday { color: var(--mid-blue); font-size: 15.5px; font-weight: 700; line-height: 17px; padding-left: 5px; padding-bottom: 1px; margin-right: 4px; border-bottom: 1px solid var(--rule-grey); }
  .weekday .en { display: block; color: var(--brand-blue); }
  .day { height: 56px; padding: 6px 0 0 7px; margin-right: 4px; font-size: 17px; font-weight: 700; color: var(--ink); border-bottom: 1px solid var(--rule-grey); }
  .day.last-row { border-bottom: none; }
</style>
</head>
<body>
<main class="page">
  <div class="hero-photo" role="img" aria-label="Rotes Mobilbagger-Fahrzeug arbeitet an einem steilen Berghang mit Latschen und Lärchen unter Dolomitenfelsen"></div>

  <svg class="frame-shapes" viewBox="0 0 1417 1417" aria-hidden="true">
    <polygon points="1320,660 1417,660 1417,1417 0,1417 0,848 990,848 1015,820 1160,820" fill="#ffffff"/>
    <polygon points="1240,603 1417,603 1417,632 1212,632" fill="#0355a3"/>
    <polygon points="905,793 1100,632 1417,632 1417,660 1200,660 1045,793" fill="#2f76bd"/>
    <polygon points="1045,793 1200,660 1320,660 1160,820 1045,820" fill="#0355a3"/>
    <rect x="0" y="793" width="1160" height="27" fill="#0355a3"/>
    <polygon points="0,820 1015,820 990,848 0,848" fill="#2f76bd"/>
    <rect x="340" y="1395" width="1077" height="22" fill="#2f76bd"/>
    <polygon points="0,1348 340,1348 365,1417 0,1417" fill="#0355a3"/>
  </svg>

  <section class="description">
    <p class="description-de">Eine unserer Hauptaktivitäten ist die Erdbewegung. Dazu gehören die Nivellierung, Aushubarbeiten für Hoch- und Tiefbauarbeiten, die Errichtung von Mauerwerk aus bewehrten Wäldern, die Landschaftsgestaltung sowie der Bau von Skipisten und Beschneiungsanlagen.</p>
    <div class="description-rule"></div>
    <p class="description-en">One of our main activities is earth movement. These include leveling, excavation work for civil engineering works, the construction of masonry from reinforced forests, landscaping and the construction of ski slopes and snowmaking equipment.</p>
  </section>

  <div class="brand">
    <span class="brand-square"></span>
    <span class="brand-name">tovel brunn</span>
  </div>
  <div class="web-address">www.tovelbrunn.it</div>

  <div class="year">2018</div>
  <div class="month">
    <div class="month-de">November</div>
    <div class="month-it">November</div>
  </div>

  <section class="calendar">
    <div class="weekend-bg sun"></div>
    <div class="weekend-bg sat"></div>
    <div class="calendar-grid">
      <div class="weekday">So<span class="en">Sun</span></div>
      <div class="weekday">Mo<span class="en">Mon</span></div>
      <div class="weekday">Di<span class="en">Tue</span></div>
      <div class="weekday">Mi<span class="en">Wed</span></div>
      <div class="weekday">Do<span class="en">Thu</span></div>
      <div class="weekday">Fr<span class="en">Fri</span></div>
      <div class="weekday">Sa<span class="en">Sat</span></div>

      <div class="day"></div><div class="day"></div><div class="day"></div><div class="day"></div>
      <div class="day">1</div><div class="day">2</div><div class="day">3</div>

      <div class="day">4</div><div class="day">5</div><div class="day">6</div><div class="day">7</div>
      <div class="day">8</div><div class="day">9</div><div class="day">10</div>

      <div class="day">11</div><div class="day">12</div><div class="day">13</div><div class="day">14</div>
      <div class="day">15</div><div class="day">16</div><div class="day">17</div>

      <div class="day">18</div><div class="day">19</div><div class="day">20</div><div class="day">21</div>
      <div class="day">22</div><div class="day">23</div><div class="day">24</div>

      <div class="day last-row">25</div><div class="day last-row">26</div><div class="day last-row">27</div><div class="day last-row">28</div>
      <div class="day last-row">29</div><div class="day last-row">30</div><div class="day last-row"></div>
    </div>
  </section>
</main>
</body>
</html>
```